Mens Gym Clothing Website - *Exciting project*

Target Market(s)

Young image conscious males who attend gym regularly

Industry/Entity Type

Clothing

Requirements
Must have
• Large image or multiple images (as fernlow) on homepage

```html
<!DOCTYPE html>
<html lang="en">
<head>
<meta charset="utf-8">
<title>Kestrel Clothing — Fitness Clothing Superstore</title>
<link href="https://fonts.googleapis.com/css2?family=Arimo:wght@400;700&family=Dosis:wght@400;500&family=Oswald:wght@500&display=swap" rel="stylesheet">
<style>
:root{
  --header-navy:#1c3954;
  --nav-blue:#2b5279;
  --hero-blue:#8fb4e0;
  --hero-pale:#c7dbf2;
  --hero-grey:#e4e6e9;
  --deep-navy:#13304e;
  --band-navy:#163654;
  --page-navy:#0f2d4a;
  --footer-grey:#2f3139;
  --footer-dark:#25262c;
  --accent-green:#8ee23a;
  --text-light:#e9eef4;
  --text-muted:#a9adb6;
  --card-text:#1f4e6e;
  --ink:#1c1c1c;
}
*{box-sizing:border-box;margin:0;padding:0}
html,body{width:1031px;height:1200px;overflow:hidden;background:var(--page-navy)}
body{font-family:"Arimo",Arial,sans-serif;color:var(--text-light);position:relative}
a{color:inherit;text-decoration:none}

.site-header{position:absolute;left:0;top:0;width:1031px;height:89px;background:linear-gradient(180deg,#24445f,var(--header-navy))}
.brand{position:absolute;left:128px;top:26px;display:flex;flex-direction:column}
.brand-name{font-weight:700;font-size:28px;letter-spacing:1px;color:#fff;line-height:30px}
.brand-tagline{font-size:14px;color:#fff;margin-top:2px}
.account-links{position:absolute;right:127px;top:7px;font-size:11px;color:#dfe6ee;display:flex;gap:10px}
.account-links span.sep{color:#9fb0c2}
.welcome{position:absolute;right:127px;top:27px;font-size:11px;color:#dfe6ee}
.search{position:absolute;left:673px;top:51px;width:225px;height:26px;display:flex;border:1px solid #0f2236}
.search-input{flex:1;background:linear-gradient(#3b5874,#2c4660)}
.search-button{width:60px;background:#1b1e24;color:#fff;font-size:11px;font-weight:700;display:flex;align-items:center;justify-content:center}

.main-nav{position:absolute;left:0;top:89px;width:1031px;height:42px;background:linear-gradient(180deg,#335d88,var(--nav-blue));border-bottom:1px solid #9bb6d2}
.main-nav ul{list-style:none;display:flex;position:absolute;left:355px;top:10px;gap:43px;font-family:"Dosis",sans-serif;font-size:19px;color:#fff}
.main-nav .current{position:relative}
.main-nav .current::after{content:"";position:absolute;left:50%;margin-left:-8px;top:32px;border:8px solid transparent;border-bottom-color:#cfdbe8;border-top:0}

.hero{position:absolute;left:0;top:131px;width:1031px;height:403px;overflow:hidden}
.hero-shapes{position:absolute;left:0;top:0}
.hero-model{position:absolute;left:373px;top:14px;width:232px;height:389px;background:linear-gradient(180deg,#2d2a2a,#151515 60%,#222);border-radius:60px 60px 0 0}
.hero-tagline{position:absolute;left:137px;top:203px;font-size:28px;color:#243648}
.support{position:absolute;left:276px;font-size:11px;color:#fff;display:flex;align-items:center;gap:12px}
.support-online{top:272px}
.support-phone{top:334px}
.support-badge{width:26px;height:28px;border-radius:50%;background:#3a3f46}
.hero-search-links{position:absolute;left:244px;top:381px;font-size:11px;color:#e6ecf2}
.hero-copy{position:absolute;left:668px;top:94px;width:232px}
.hero-copy h2{font-weight:400;font-size:26px;color:var(--accent-green);letter-spacing:.5px}
.hero-copy p{font-size:10px;line-height:15px;color:#fff;margin-top:12px}
.read-more{position:absolute;left:707px;top:239px;width:158px;height:31px;border-radius:6px;background:linear-gradient(#2b2b2b,#0c0c0c);color:#fff;font-weight:700;font-size:15px;display:flex;align-items:center;justify-content:center;box-shadow:0 2px 4px rgba(0,0,0,.4)}
.read-more::before{content:"";position:absolute;left:71px;top:-9px;border:9px solid transparent;border-bottom-color:#2b2b2b;border-top:0}
.slide-dots{position:absolute;left:825px;top:382px;display:flex;gap:4px}
.slide-dots i{width:10px;height:10px;border-radius:50%;background:#3a3f47;display:block}
.slide-dots i.active{background:var(--accent-green)}

.perks{position:absolute;left:0;top:534px;width:1031px;height:122px;background:var(--band-navy);border-bottom:4px solid #24476a}
.perk{position:absolute;top:34px;display:flex;gap:14px}
.perk-icon{width:74px;height:56px;border-radius:8px}
.perk h3{font-weight:400;font-size:14px;color:#fff;margin-bottom:8px}
.perk p{font-size:10px;line-height:15px;color:#fff;width:150px}
.perk-delivery{left:130px}
.perk-delivery .perk-icon{background:linear-gradient(#5a7895,#d9791e);height:42px;margin-top:0}
.perk-gift{left:420px}
.perk-gift .perk-icon{width:50px;background:linear-gradient(#a4d63a,#6f9d18)}
.perk-student{left:648px}
.perk-student .perk-icon{width:60px;height:60px;border-radius:50%;background:radial-gradient(circle at 40% 35%,#4fa2ea,#1557a8)}

.feature-cards{position:absolute;left:0;top:660px;width:1031px;height:335px}
.card{position:absolute;top:14px;width:212px;height:290px;background:#fff;border:1px solid #fff;outline:1px solid #2b2b2b;outline-offset:-4px;box-shadow:4px 4px 6px rgba(0,0,0,.5);text-align:center;color:var(--ink)}
.card-photo{margin:10px auto 0;width:132px;height:133px;background:linear-gradient(180deg,#cfa98c 0,#cfa98c 28%,#4c6663 30%,#3b5553);border-radius:40px 40px 0 0}
.card-rule{border-top:1px dotted #555;margin:0 3px}
.card-rule.upper{margin-top:-19px}
.card-rule.lower{margin-top:19px}
.card h3{font-weight:400;font-size:16px;margin-top:19px}
.card p{font-size:11px;line-height:13px;color:var(--card-text);margin:14px auto 0;width:180px}
.card-button{display:inline-flex;align-items:center;justify-content:center;width:84px;height:32px;margin-top:15px;border:1px solid #c4c4c4;border-radius:3px;background:linear-gradient(#fafafa,#dedede);color:#444;font-size:13px}
.card-top{left:134px}
.card-blog{left:397px}
.card-offers{left:662px}
.card-offers h3{margin-top:26px}

.site-footer{position:absolute;left:0;top:995px;width:1031px;height:163px;background:var(--footer-grey);border-top:1px solid #3d4049}
.about{position:absolute;left:132px;top:11px;width:238px}
.about h4{font-weight:400;font-size:11px;color:#fff;margin-bottom:9px}
.about p{font-size:9px;line-height:14px;color:var(--text-muted)}
.footer-links{position:absolute;top:30px;list-style:none;font-size:10px;color:#d8dce2}
.footer-links li{height:22px;padding-left:16px;position:relative}
.footer-links li::before{content:"";position:absolute;left:0;top:3px;width:7px;height:6px;background:#9dc4e6;clip-path:polygon(0 30%,55% 30%,55% 0,100% 50%,55% 100%,55% 70%,0 70%)}
.links-service{left:438px}
.links-extra{left:595px}
.newsletter{position:absolute;left:719px;top:10px;width:175px}
.newsletter h4{font-family:"Oswald",sans-serif;font-weight:500;font-size:14px;color:#fff;letter-spacing:.5px}
.newsletter p{font-size:10px;color:#e2e5ea;margin-top:13px}
.newsletter-input{margin-top:8px;height:23px;border:1px solid #1a1b20;background:#26282e}
.subscribe{margin:5px 0 0 auto;width:54px;height:24px;background:#1a1b20;color:#fff;font-size:9px;display:flex;align-items:center;justify-content:center}
.social{display:flex;gap:8px;margin-top:8px;margin-left:8px}
.social span{width:28px;height:28px;border-radius:5px;background:#17181c;border:1px solid #3d3f46}

.legal-bar{position:absolute;left:0;top:1158px;width:1031px;height:42px;background:var(--footer-dark);font-size:10px;color:#d8dce2}
.copyright{position:absolute;left:126px;top:15px}
.legal-links{position:absolute;right:128px;top:15px;display:flex;gap:8px}
</style>
</head>
<body>

<header class="site-header">
  <a class="brand" href="#">
    <span class="brand-name">KESTREL CLOTHING</span>
    <span class="brand-tagline">The No.1 Fitness Clothing Superstore</span>
  </a>
  <nav class="account-links">
    <a href="#">My Account</a><span class="sep">I</span>
    <a href="#">My Wishlist</a><span class="sep">I</span>
    <a href="#">My Cart</a><span class="sep">I</span>
    <a href="#">Checkout</a><span class="sep">I</span>
    <a href="#">Log In</a>
  </nav>
  <p class="welcome">Welcome to our online store !</p>
  <form class="search">
    <div class="search-input"></div>
    <div class="search-button">Search</div>
  </form>
</header>

<nav class="main-nav">
  <ul>
    <li class="current">Home</li>
    <li>Brands</li>
    <li>Clothing</li>
    <li>FAQ</li>
    <li>News &amp; Stock Updates</li>
  </ul>
</nav>

<section class="hero">
  <svg class="hero-shapes" width="1031" height="403" viewBox="0 0 1031 403" aria-hidden="true">
    <defs>
      <linearGradient id="heroSky" x1="0" y1="0" x2="1" y2="0.3">
        <stop offset="0" stop-color="#7da5d6"/>
        <stop offset="0.6" stop-color="#9dbde6"/>
        <stop offset="1" stop-color="#b7cff0"/>
      </linearGradient>
      <linearGradient id="heroGrey" x1="0" y1="0" x2="1" y2="1">
        <stop offset="0" stop-color="#f0f1f3"/>
        <stop offset="1" stop-color="#cfd2d6"/>
      </linearGradient>
    </defs>
    <rect width="1031" height="403" fill="url(#heroSky)"/>
    <polygon points="0,0 121,0 342,221 161,403 0,403" fill="url(#heroGrey)"/>
    <polygon points="161,403 342,221 523,403" fill="#13304e"/>
  </svg>
  <div class="hero-model" role="img" aria-label="Model in a dark suit and red tie"></div>
  <p class="hero-tagline">Tagline--</p>
  <div class="support support-online"><span class="support-badge" role="img" aria-label="Online support agent"></span>Online Support</div>
  <div class="support support-phone">
    <svg width="26" height="26" viewBox="0 0 24 24" aria-hidden="true"><path d="M6.6 10.8a15 15 0 0 0 6.6 6.6l2.2-2.2c.3-.3.7-.4 1-.2 1.1.4 2.3.6 3.6.6.6 0 1 .4 1 1V20c0 .6-.4 1-1 1A17 17 0 0 1 3 4c0-.6.4-1 1-1h3.5c.6 0 1 .4 1 1 0 1.3.2 2.5.6 3.6.1.3 0 .7-.2 1z" fill="#dfe3e8"/></svg>
    Telephonic Support
  </div>
  <p class="hero-search-links">Search by Categories | Search by Brand</p>
  <div class="hero-copy">
    <h2>LOREM IPSUM</h2>
    <p>Lorem ipsum dolor sit amet, consectetur adipiscing elit. Curabitur non posuere nibh. In faucibus sapien non nunc sollicitudin nec consectetur nisi vestibulum. Vestibulum eget dui dolor. Donec id venenatis ligula. Curabitur blandit blandit erat.</p>
  </div>
  <a class="read-more" href="#">Read More....</a>
  <div class="slide-dots"><i></i><i></i><i class="active"></i><i></i><i></i></div>
</section>

<section class="perks">
  <div class="perk perk-delivery">
    <div class="perk-icon" role="img" aria-label="Delivery truck"></div>
    <div><h3>Free Delivery Worldwide</h3><p>Lorem ipsum dolor sit amet, consectetur adipiscing elit. Curabitur non posuere nibh.</p></div>
  </div>
  <div class="perk perk-gift">
    <div class="perk-icon" role="img" aria-label="Wrapped gift box"></div>
    <div><h3>Gift Vouchers</h3><p>Lorem ipsum dolor sit amet, consectetur adipiscing elit. Curabitur non posuere nibh.</p></div>
  </div>
  <div class="perk perk-student">
    <div class="perk-icon" role="img" aria-label="Twenty percent discount sticker"></div>
    <div><h3>Student Discount</h3><p>Lorem ipsum dolor sit amet, consectetur adipiscing elit. Curabitur non posuere nibh.</p></div>
  </div>
</section>

<section class="feature-cards">
  <article class="card card-top">
    <div class="card-photo" role="img" aria-label="Model in a green button-up shirt"></div>
    <div class="card-rule upper"></div><div class="card-rule lower"></div>
    <h3>Top Ten</h3>
    <p>Your edit of what's new on site</p>
    <a class="card-button" href="#">Shop Now</a>
  </article>
  <article class="card card-blog">
    <div class="card-photo" role="img" aria-label="Model in a green button-up shirt"></div>
    <div class="card-rule upper"></div><div class="card-rule lower"></div>
    <h3>Latest Blog</h3>
    <p>Served fresh every day because you can never have too much on your plate</p>
    <a class="card-button" href="#">View Now</a>
  </article>
  <article class="card card-offers">
    <div class="card-photo" role="img" aria-label="Model in a green button-up shirt"></div>
    <div class="card-rule upper"></div><div class="card-rule lower"></div>
    <h3>Latest Offers</h3>
    <p>Your edit of what's new on site</p>
    <a class="card-button" href="#">Shop Now</a>
  </article>
</section>

<footer class="site-footer">
  <div class="about">
    <h4>About Us</h4>
    <p>Lorem ipsum dolor sit amet, consectetur adipiscing elit, sed do eiusmod tempor incididunt ut labore et dolore magna aliqua. Ut enim ad minim veniam, quis nostrud exercitation ullamco laboris nisi ut aliquip ex ea commodo consequat. Duis aute irure dolor in reprehenderit in voluptate velit esse cillum dolore eu fugiat nulla pariatur. Excepteur sint occaecat cupidatat non proident, sunt in culpa qui officia deserunt mollit anim id est laborum</p>
  </div>
  <ul class="footer-links links-service">
    <li>Customer Service</li><li>Why Us</li><li>Search Terms</li><li>Contact Us</li>
  </ul>
  <ul class="footer-links links-extra">
    <li>Link 1</li><li>Link 2</li><li>Link 3</li><li>Link 4</li>
  </ul>
  <div class="newsletter">
    <h4>NEWSLETTER</h4>
    <p>Subscribe for Our Newsletter:</p>
    <div class="newsletter-input"></div>
    <div class="subscribe">Subscribe</div>
    <div class="social"><span></span><span></span><span></span><span></span><span></span></div>
  </div>
</footer>

<div class="legal-bar">
  <p class="copyright">Copyright © 2011 All rights reserved.</p>
  <nav class="legal-links">
    <a href="#">Site Map</a><span>|</span>
    <a href="#">Search Terms</a><span>|</span>
    <a href="#">Advanced Search</a><span>|</span>
    <a href="#">Contact Us</a>
  </nav>
</div>

</body>
</html>
```